Bright Arch Group business card

Bright Arch Group is the parent company of Bright Arch Building, Bright Arch Plumbing and Bright Arch Renovating. We require a sophisticated business card that covers all aspects of the building and plumbing space without using told or construction items.

Industry/Entity Type

Construction Company

Contact Information for Business Card

Warrick Hadley
Director
0455921834
warrick@brightarch.com.au
Www.brightarch.com.au

Font styles to use
Serif
Sans Serif

Colors
3176b5
ffce3e
0692cd
34a7d8
fbee3e
faa54b

Requirements
Must have
• Logo on front
• Logo and details on rear.
Nice to have
• Maybe water mark or shadow effect with logo
Should not have
• Tools or any construction associated items

```html
<!DOCTYPE html>
<html lang="en">
<head>
<meta charset="utf-8">
<title>Bright Arch Group – Business Card</title>
<link rel="stylesheet" href="https://fonts.googleapis.com/css2?family=Jost:wght@300;400;700&display=swap">
<style>
  :root {
    --backdrop: #2e2e2e;
    --card-blue: #1a5e92;
    --sky: #00a8e8;
    --accent-orange: #f0890f;
    --ink: #0d0d0d;
    --white: #ffffff;
  }
  * { margin: 0; padding: 0; box-sizing: border-box; }
  html, body {
    width: 1192px; height: 1200px; overflow: hidden;
    background: var(--backdrop);
    font-family: "Jost", sans-serif;
  }
  .card {
    position: absolute; left: 166px; width: 850px; height: 472px;
    background: var(--card-blue); overflow: hidden;
    box-shadow: 0 6px 18px rgba(0,0,0,.55);
  }
  .card--front { top: 88px; }
  .card--back { top: 638px; }

  .rule { position: absolute; height: 4px; background: var(--white); }
  .card--front .rule { left: 0; top: 414px; width: 562px; }
  .card--back .rule { left: 455px; top: 414px; width: 395px; }

  .wordmark {
    position: absolute; display: flex; align-items: center; gap: 16px;
    color: var(--ink); font-weight: 300; text-transform: uppercase;
  }
  .wordmark__dot { flex: none; border-radius: 50%; background: var(--accent-orange); }
  .wordmark__name { line-height: 1.05; text-align: center; }
  .wordmark__name span { display: block; }

  .card--front .wordmark { left: 0; width: 850px; top: 200px; justify-content: center; }
  .card--front .wordmark__dot { width: 34px; height: 34px; }
  .card--front .wordmark__name { font-size: 48px; letter-spacing: 12px; }
  .card--front .wordmark__name span + span { font-size: 34px; letter-spacing: 22px; }

  .card--back .wordmark { left: 520px; width: 300px; top: 262px; justify-content: center; gap: 12px; }
  .card--back .wordmark__dot { width: 22px; height: 22px; }
  .card--back .wordmark__name { font-size: 29px; letter-spacing: 6px; }
  .card--back .wordmark__name span + span { font-size: 22px; letter-spacing: 14px; }

  .holder-name {
    position: absolute; left: 60px; top: 214px;
    font-size: 48px; font-weight: 700; color: var(--sky); letter-spacing: .5px;
  }
  .contact { position: absolute; list-style: none; color: var(--white); font-size: 22px; font-weight: 400; }
  .contact li { position: absolute; display: flex; align-items: center; gap: 14px; white-space: nowrap; }
  .contact svg { width: 22px; height: 22px; fill: var(--white); flex: none; }
  .contact__role { left: 98px; top: 288px; }
  .contact__phone { left: 136px; top: 325px; }
  .contact__email { left: 148px; top: 362px; }
  .contact__web { left: 140px; top: 400px; }
</style>
</head>
<body>

<section class="card card--front" aria-label="Card front">
  <div class="wordmark">
    <div class="wordmark__dot"></div>
    <div class="wordmark__name"><span>Bright Arch</span><span>Group</span></div>
  </div>
  <div class="rule"></div>
</section>

<section class="card card--back" aria-label="Card back">
  <h1 class="holder-name">Warrick Hadley</h1>
  <ul class="contact">
    <li class="contact__role">
      <svg viewBox="0 0 24 24"><circle cx="12" cy="7" r="5"/><path d="M2 23c0-6 4.5-9 10-9s10 3 10 9z"/></svg>Director
    </li>
    <li class="contact__phone">
      <svg viewBox="0 0 24 24"><path d="M6.6 10.8a15 15 0 0 0 6.6 6.6l2.2-2.2a1 1 0 0 1 1-.25 11.4 11.4 0 0 0 3.6.57 1 1 0 0 1 1 1V20a1 1 0 0 1-1 1A17 17 0 0 1 3 4a1 1 0 0 1 1-1h3.5a1 1 0 0 1 1 1c0 1.25.2 2.45.57 3.57a1 1 0 0 1-.25 1z"/></svg>0455 921 834
    </li>
    <li class="contact__email">
      <svg viewBox="0 0 24 24"><path d="M2 5h20v2l-10 6L2 7z"/><path d="M2 9l10 6 10-6v10H2z"/></svg>warrick@brightarch.com.au
    </li>
    <li class="contact__web">
      <svg viewBox="0 0 24 24"><circle cx="12" cy="12" r="10"/><path d="M12 2v20M2 12h20" stroke="#1a5e92" stroke-width="1.6" fill="none"/></svg>Www.brightarch.com.au
    </li>
  </ul>
  <div class="wordmark">
    <div class="wordmark__dot"></div>
    <div class="wordmark__name"><span>Bright Arch</span><span>Group</span></div>
  </div>
  <div class="rule"></div>
</section>

</body>
</html>
```